Business card

would like a double sided business card made up with my logos provided.
Prefer card to have black background and to use the black logos, with matching blue writing for the text.
One side to just be the logo, (Try to use both the black logos)
the other side to have the logo and also my credentials/business information.

Covering all aspects of Carpentry and Building Services

Marcus Tolvey
Qualified Carpenter
Mob: 0417263948
Email: rkt.joinery@mailbright.com
ABN: 47 615 209 834

Industry/Entity Type

Business

Contact Information for Business Card

Marcus Tolvey
Qualified Carpenter
Mob: 0417263948
ABN: 47 615 209 834

Requirements
Must have
• Please try to use both the black logos and incorporate into the card.

```html
<!DOCTYPE html>
<html lang="en">
<head>
<meta charset="utf-8">
<title>RKT Joinery – Business Card</title>
<link rel="stylesheet" href="https://fonts.googleapis.com/css2?family=Open+Sans:wght@400;600;700&display=swap">
<style>
  :root {
    --backdrop: #b9c0c8;
    --card: #ffffff;
    --navy: #27347a;
    --blue: #2f86c4;
    --blue-light: #3aa0dc;
    --ink: #2b2b2b;
    --swoosh: #1e1e22;
  }
  * { box-sizing: border-box; margin: 0; padding: 0; }
  html, body { width: 1200px; height: 700px; overflow: hidden; }
  body {
    background: var(--backdrop);
    font-family: "Open Sans", Arial, sans-serif;
    position: relative;
  }
  .card {
    position: absolute;
    top: 207px;
    width: 500px;
    height: 286px;
    background: var(--card);
    overflow: hidden;
    box-shadow: 0 10px 24px rgba(0,0,0,0.25);
  }
  .card--info { left: 70px; }
  .card--logo { left: 630px; }
  .card__wave { position: absolute; inset: 0; width: 100%; height: 100%; }

  .brand {
    position: absolute;
    display: flex;
    align-items: center;
    gap: 10px;
    color: var(--ink);
    font-weight: 700;
    letter-spacing: 0.5px;
    white-space: nowrap;
  }
  .brand__mark { background: var(--blue); display: block; }
  .card--logo .brand { left: 140px; top: 82px; font-size: 38px; }
  .card--logo .brand__mark { width: 22px; height: 22px; }
  .card--info .brand { left: 36px; top: 44px; font-size: 24px; }
  .card--info .brand__mark { width: 14px; height: 14px; }

  .divider {
    position: absolute;
    left: 214px; top: 40px;
    width: 2px; height: 96px;
    background: var(--blue);
  }
  .divider--h {
    left: 36px; top: 112px;
    width: 150px; height: 2px;
  }

  .contact {
    position: absolute;
    left: 234px; top: 42px;
    list-style: none;
    font-size: 13px;
    color: var(--ink);
    line-height: 21px;
  }
  .contact li { display: flex; align-items: center; gap: 7px; }
  .contact svg { width: 11px; height: 11px; flex: none; }
  .contact .address { padding-left: 18px; }

  .holder {
    position: absolute;
    right: 24px; bottom: 16px;
    text-align: right;
    color: #ffffff;
  }
  .holder__name { font-size: 17px; font-weight: 700; }
  .holder__role { font-size: 15px; font-weight: 400; }
</style>
</head>
<body>

  <section class="card card--info">
    <svg class="card__wave" viewBox="0 0 500 286" preserveAspectRatio="none" aria-hidden="true">
      <defs>
        <linearGradient id="waveBlueA" x1="0" y1="0" x2="1" y2="0">
          <stop offset="0" stop-color="#1f5d9e"/>
          <stop offset="0.5" stop-color="#3aa0dc"/>
          <stop offset="1" stop-color="#27347a"/>
        </linearGradient>
      </defs>
      <path d="M0,150 C110,205 260,230 500,222 L500,286 L0,286 Z" fill="url(#waveBlueA)"/>
      <path d="M0,182 C130,238 290,248 500,236 L500,286 L0,286 Z" fill="var(--navy)"/>
      <path d="M0,140 C110,198 270,226 500,214" fill="none" stroke="var(--swoosh)" stroke-width="4"/>
      <path d="M0,132 C110,190 270,218 500,207" fill="none" stroke="var(--blue-light)" stroke-width="1.2"/>
    </svg>

    <div class="brand"><span class="brand__mark"></span>RKT Joinery</div>
    <div class="divider divider--h"></div>
    <div class="divider"></div>

    <ul class="contact">
      <li>
        <svg viewBox="0 0 12 12" aria-hidden="true"><rect x="3" y="0.5" width="6" height="11" rx="1" fill="none" stroke="#666" stroke-width="1.2"/><circle cx="6" cy="9.5" r="0.8" fill="#666"/></svg>
        <span>: 0417263948</span>
      </li>
      <li>
        <svg viewBox="0 0 12 12" aria-hidden="true"><circle cx="6" cy="6" r="5" fill="none" stroke="#666" stroke-width="1.2"/><rect x="4" y="4" width="4" height="4" fill="none" stroke="#666" stroke-width="1"/></svg>
        <span>: 47 615 209 834</span>
      </li>
      <li>
        <svg viewBox="0 0 12 12" aria-hidden="true"><rect x="0.6" y="2.5" width="10.8" height="7.5" fill="none" stroke="#666" stroke-width="1.2"/><path d="M0.6,2.5 L6,7 L11.4,2.5" fill="none" stroke="#666" stroke-width="1.1"/></svg>
        <span>: rkt.joinery@mailbright.com</span>
      </li>
      <li class="address">Street Name, City Name</li>
      <li class="address">Zip Code-00000</li>
    </ul>

    <div class="holder">
      <p class="holder__name">Marcus Tolvey</p>
      <p class="holder__role">Qualified Carpenter</p>
    </div>
  </section>

  <section class="card card--logo">
    <svg class="card__wave" viewBox="0 0 500 286" preserveAspectRatio="none" aria-hidden="true">
      <defs>
        <linearGradient id="waveBlueB" x1="0" y1="0" x2="1" y2="0">
          <stop offset="0" stop-color="#1f5d9e"/>
          <stop offset="0.5" stop-color="#3aa0dc"/>
          <stop offset="1" stop-color="#27347a"/>
        </linearGradient>
      </defs>
      <path d="M0,150 C110,205 260,230 500,222 L500,286 L0,286 Z" fill="url(#waveBlueB)"/>
      <path d="M0,182 C130,238 290,248 500,236 L500,286 L0,286 Z" fill="var(--navy)"/>
      <path d="M0,140 C110,198 270,226 500,214" fill="none" stroke="var(--swoosh)" stroke-width="4"/>
      <path d="M0,132 C110,190 270,218 500,207" fill="none" stroke="var(--blue-light)" stroke-width="1.2"/>
    </svg>

    <div class="brand"><span class="brand__mark"></span>RKT Joinery</div>
  </section>

</body>
</html>
```